School annual plan - describing all our goals for 2026

This is a high school plan. The design should be similar in style to other school flyers and posters.

2026 Tallow SHS AIP - the document to design. Please make 1 page.

Documents to follow style:
Document 1: the 2025 School Annual Plan (use this for formatting. Change style to similar to Documents 2 & 3).

Document 2: the Tallow Instructional Model - make the style similar to this.

Document 3: Explicit Instruction Classroom Matrix - Another document to make the style similar to.

This is the school's website: https://tallowshs.qz.edu.au/

Please let me know if you have any questions.

```html
<!DOCTYPE html>
<html lang="en">
<head>
<meta charset="utf-8">
<title>Tallow State High School – 2026 Annual Implementation Plan</title>
<link rel="stylesheet" href="https://fonts.googleapis.com/css2?family=Roboto+Condensed:wght@400;500;700;800;900&family=Montserrat:wght@800&display=swap">
<style>
:root{
  --navy:#263a7a;
  --navy-dark:#1f2f66;
  --yellow:#f4e77a;
  --yellow-text:#f2e36b;
  --cream:#fdf9e1;
  --ice:#e7ecf8;
  --sky:#b9c6e6;
  --ink:#1f2b5c;
  --white:#ffffff;
}
*{box-sizing:border-box;margin:0;padding:0}
html,body{width:1200px;height:882px;overflow:hidden;background:var(--white)}
body{font-family:"Roboto Condensed",Arial,sans-serif;color:var(--ink);position:relative}
.block{position:absolute}
.site-header{position:absolute;left:0;top:0;width:1200px;height:92px}
.header-band{position:absolute;left:87px;top:0;width:1113px;height:92px;background:var(--navy);z-index:0}
.brand{position:absolute;left:8px;top:36px;width:76px;z-index:2;display:flex;align-items:center;gap:5px;font-weight:800;font-size:16px;line-height:1;color:var(--navy)}
.brand-dot{flex:none;width:11px;height:11px;border-radius:50%;background:var(--yellow)}
.school-title{position:absolute;left:152px;top:25px;z-index:1;font-weight:900;font-size:41px;letter-spacing:.2px;color:var(--white);line-height:1;white-space:nowrap}
.year-pill{position:absolute;left:694px;top:35px;z-index:2;width:90px;height:38px;border:2px solid var(--white);border-radius:20px 0 0 20px;background:var(--navy);color:var(--white);font-family:"Montserrat",sans-serif;font-weight:800;font-size:22px;display:flex;align-items:center;justify-content:center}
.plan-strip{position:absolute;left:784px;top:36px;z-index:1;width:416px;height:36px;background:var(--yellow);color:var(--navy);font-family:"Montserrat",sans-serif;font-weight:800;font-size:20px;display:flex;align-items:center;padding-left:10px;letter-spacing:.3px;white-space:nowrap}
.navy{background:var(--navy);color:var(--white)}
.cream{background:var(--cream)}
.ice{background:var(--ice)}
.yellow{background:var(--yellow)}
.sky{background:var(--sky)}
.priority-no{display:flex;align-items:center;justify-content:center;gap:3px;border-radius:8px 0 0 0}
.priority-no .num{font-weight:900;font-size:38px;color:var(--yellow-text);line-height:1}
.priority-no .lbl{font-weight:800;font-size:12px;line-height:1.05}
.priority-title{padding:8px 11px}
.priority-title h2{font-weight:800;font-size:13px;color:var(--yellow-text);line-height:1.15}
.priority-title .sub{margin-top:5px;padding-top:4px;border-top:1px solid #5a6ba3;font-size:7px;color:var(--white);line-height:1.25}
.priority-title .sub b{color:var(--yellow-text)}
.monitoring{display:flex;flex-direction:column}
.monitoring h3{font-weight:800;font-size:13px;color:var(--yellow-text);text-align:center;padding:6px 0 4px;border-bottom:1px solid #5a6ba3}
.terms{display:flex;gap:3px;padding:3px 0 0 0;flex:1}
.term{flex:1;font-size:7px;font-weight:700;color:var(--navy);display:flex;align-items:center;justify-content:center}
.term.a{background:var(--yellow)}.term.b{background:var(--sky)}
.row-label{display:flex;align-items:center;padding-left:12px;font-weight:700;font-size:7.6px;line-height:1.25;border-radius:6px 0 0 6px}
.content{padding:8px 11px;font-size:6.6px;line-height:1.38;border-radius:0 6px 6px 0}
.content h4{font-weight:700;font-size:7.4px;margin-bottom:4px;color:var(--navy)}
ul.ticks{list-style:none}
ul.ticks li{position:relative;padding-left:8px}
ul.ticks li::before{content:"";position:absolute;left:0;top:2.4px;width:4px;height:4px;border-radius:50%;background:var(--navy)}
.cols{display:flex;gap:14px}
.bar{display:flex;align-items:center;padding-left:8px;font-size:7.4px;font-weight:700;border-radius:4px}
.bar b{color:var(--yellow-text)}
.bar.center{justify-content:center;padding:0;color:var(--yellow-text)}
.panel{padding:8px 10px;font-size:6.6px;line-height:1.38}
.panel.rounded-bl{border-radius:0 0 0 8px}
.panel.rounded-br{border-radius:0 0 8px 0}
.vertical{display:flex;align-items:center;justify-content:center}
.vertical span{transform:rotate(-90deg);white-space:nowrap;font-weight:700;font-size:9px;letter-spacing:.3px}
.measure{padding:10px 10px;font-size:6.6px;line-height:1.4}
.measure h4{font-weight:700;font-size:7.4px;line-height:1.3;margin-bottom:5px;color:var(--navy)}
.measure h4 .hl{color:#3650a8}
.redtape-label{display:flex;align-items:center;padding-left:10px;font-weight:700;font-size:7.6px;line-height:1.3}
.redtape{border:1px solid var(--navy);padding:9px 12px;display:flex;gap:0;font-size:6.6px;line-height:1.45}
.redtape ul{flex:1}
svg.rules{position:absolute;left:0;top:0}
</style>
</head>
<body>

<header class="site-header">
  <div class="header-band"></div>
  <div class="brand"><span class="brand-dot"></span>Tallow</div>
  <h1 class="school-title">TALLOW STATE HIGH SCHOOL</h1>
  <div class="year-pill">2026</div>
  <div class="plan-strip">ANNUAL IMPLEMENTATION PLAN</div>
</header>

<svg class="rules" width="1200" height="882" viewBox="0 0 1200 882" aria-hidden="true">
  <g fill="none" stroke="var(--navy)" stroke-width="1">
    <path d="M610 114 V432 Q610 443 600 443 H36"/>
    <path d="M610 432 Q610 443 620 443 H1165"/>
    <path d="M610 722 V778 Q610 789 600 789 H115"/>
    <path d="M610 778 Q610 789 620 789 H1165"/>
  </g>
  <g fill="var(--navy)">
    <circle cx="610" cy="114" r="3.5"/><circle cx="34" cy="443" r="3.5"/><circle cx="1167" cy="443" r="3.5"/>
    <circle cx="610" cy="722" r="3.5"/><circle cx="1167" cy="789" r="3.5"/>
  </g>
</svg>

<!-- Priority 1 -->
<section>
  <div class="block navy priority-no" style="left:34px;top:118px;width:81px;height:58px"><span class="num">1</span><span class="lbl">SCHOOL<br>PRIORITY</span></div>
  <div class="block navy priority-title" style="left:117px;top:118px;width:338px;height:58px">
    <h2>BELONGING AND ENGAGEMENT</h2>
    <p class="sub"><b>IN CLASSROOMS:</b> PEDAGOGY-WHOLE SCHOOL FOCUS ON PEDAGOGY AND<br><b>"HOW TALLOW STUDENTS LEARN"</b></p>
  </div>
  <div class="block navy monitoring" style="left:458px;top:118px;width:142px;height:58px">
    <h3>MONITORING</h3>
    <div class="terms" style="background:var(--white)"><span class="term a">TERM 1</span><span class="term b">TERM 2</span><span class="term a">TERM 3</span><span class="term b">TERM 4</span></div>
  </div>

  <div class="block navy row-label" style="left:34px;top:180px;width:81px;height:79px">LINK TO<br>SCHOOL<br>IMPROVEMENT<br>STRATEGY</div>
  <div class="block ice content" style="left:117px;top:180px;width:483px;height:79px">
    <h4>OUR 2026 FOCUS AREA FOR IMPROVEMENT IS TO:</h4>
    <ul class="ticks">
      <li>Enact planned and intentional pedagogical practices that align to How Tallow Students Learn</li>
      <li>Conduct regular in-class observation and feedback cycles</li>
      <li>Deliver intensive pedagogy support for teachers using classroom profiling, walkthroughs and structured feedback in explicit instruction pedagogy</li>
      <li>Adopt clear processes to track, monitor and differentiate support so that every child is learning and improving</li>
      <li>Drive Digital Innovation through the integration of SkyLearn.</li>
    </ul>
  </div>

  <div class="block navy row-label" style="left:34px;top:263px;width:81px;height:64px">STRATEGIES</div>
  <div class="block cream content" style="left:117px;top:263px;width:483px;height:64px">
    <ul class="ticks">
      <li>Line Management, quality assurance, setting professional goals (SPG)</li>
      <li>Observation and Feedback Framework</li>
      <li>Classroom Profiling</li>
      <li>Differentiated approaches to pedagogy</li>
      <li>Digital Pedagogy</li>
    </ul>
  </div>

  <div class="block navy bar" style="left:34px;top:329px;width:421px;height:16px"><b>ACTIONS:</b>&nbsp;INCLUDING RESPONSIBLE ROLE(S)</div>
  <div class="block navy bar center" style="left:458px;top:329px;width:142px;height:16px">RESOURCES</div>
  <div class="block ice panel rounded-bl" style="left:34px;top:349px;width:421px;height:86px">
    <ul class="ticks">
      <li>Enact planned and intentional pedagogical practices that align to How Tallow Students Learn</li>
      <li>Conduct regular in-class observation and feedback cycles</li>
      <li>Deliver intensive pedagogy support for teachers using classroom profiling, walkthroughs and structured feedback in explicit instruction pedagogy</li>
      <li>Adopt clear processes to track, monitor and differentiate support so that every child is learning and improving</li>
      <li>Drive Digital Innovation through the integration of SkyLearn.</li>
    </ul>
  </div>
  <div class="block cream panel rounded-br" style="left:458px;top:349px;width:142px;height:86px">
    <ul class="ticks">
      <li>Tallow HITS</li><li>Critical Routines</li><li>ESCMs</li><li>How Tallow Students Learn</li>
      <li>Classroom Observation and Feedback Cycle</li><li>MTSS documents</li>
    </ul>
  </div>
</section>

<!-- Priority 2 -->
<section>
  <div class="block navy priority-no" style="left:622px;top:118px;width:81px;height:58px"><span class="num">2</span><span class="lbl">SCHOOL<br>PRIORITY</span></div>
  <div class="block navy priority-title" style="left:706px;top:118px;width:315px;height:58px;padding-top:14px">
    <h2>CURRICULUM- CONTINUED IMPROVEMENT<br>YEAR 7-12 CURRICULUM</h2>
  </div>
  <div class="block navy monitoring" style="left:1025px;top:118px;width:142px;height:58px">
    <h3>MONITORING</h3>
    <div class="terms" style="background:var(--white)"><span class="term a">TERM 1</span><span class="term b">TERM 2</span><span class="term a">TERM 3</span><span class="term b">TERM 4</span></div>
  </div>

  <div class="block navy row-label" style="left:622px;top:180px;width:81px;height:79px">LINK TO<br>SCHOOL<br>IMPROVEMENT<br>STRATEGY</div>
  <div class="block ice content" style="left:706px;top:180px;width:461px;height:79px">
    <h4>OUR 2026 FOCUS AREA FOR IMPROVEMENT IS TO:</h4>
    <ul class="ticks">
      <li>Deliver an aligned and engaging curriculum that is regularly reviewed as part of a quality assurance cycle</li>
      <li>Enact a Whole-School Moderation Policy ensuring alignment, validity, and reliability of teacher judgments: before, after, end</li>
      <li>Deepen the school's Reading Strategy under MTSS, targeting Tier 1, 2, and 3 interventions</li>
      <li>Complete full alignment to Australian Curriculum V9, ensuring consistency across Years 7–10</li>
      <li>Strengthen SCE attainment and pathways monitoring for Years 10–12 students.</li>
    </ul>
  </div>

  <div class="block navy row-label" style="left:622px;top:263px;width:81px;height:64px">STRATEGIES</div>
  <div class="block cream content cols" style="left:706px;top:263px;width:461px;height:64px">
    <ul class="ticks">
      <li>Teaching and Learning- all HoD aligned</li><li>Line Management- quality assurance</li>
      <li>Whole school walk-throughs</li><li>Moderation- before, after, end</li><li>Whole School Reading Strategy</li>
    </ul>
    <ul class="ticks">
      <li>V9 Australian Curriculum with accessible assessment</li><li>Maximising Learning Team and collaboration time</li>
      <li>Widen VET options in Senior School</li><li>Senior School Pathways document.</li>
    </ul>
  </div>

  <div class="block navy bar" style="left:622px;top:329px;width:400px;height:16px"><b>ACTIONS:</b>&nbsp;INCLUDING RESPONSIBLE ROLE(S)</div>
  <div class="block navy bar center" style="left:1025px;top:329px;width:142px;height:16px">RESOURCES</div>
  <div class="block ice panel rounded-bl" style="left:622px;top:349px;width:400px;height:86px">
    <ul class="ticks">
      <li>Continue to embed SkyLearn as the core platform for curriculum programs, and resources in Year 7 &amp; 8 Core, VET and Year 11 &amp; 12 for assessment submission</li>
      <li>Continue implementation of Australian Curriculum V9</li>
      <li>Continue to deliver 2024 SCAA Applied syllabuses and 2025 SCAA General syllabuses</li>
      <li>Increase VET options to meet the needs of our learners, priority in Year 10 2026</li>
      <li>Enact differentiated curriculum that meets the individual needs of students in classrooms</li>
    </ul>
  </div>
  <div class="block cream panel rounded-br" style="left:1025px;top:349px;width:142px;height:86px;padding-top:5px">
    <ul class="ticks">
      <li>SkyLearn</li><li>ClassHub</li><li>Data Plan</li><li>StudyPath NCRA</li><li>SCAA</li>
      <li>CARF- K-12 Framework</li><li>Dept Curriculum Portal</li><li>Skills Register</li>
    </ul>
  </div>
</section>

<!-- Success criteria -->
<section>
  <div class="block navy vertical" style="left:34px;top:455px;width:21px;height:334px;border-radius:6px 0 0 6px"><span>END OF YEAR SUCCESS CRITERIA</span></div>
  <div class="block navy vertical" style="left:57px;top:455px;width:55px;height:262px"><span>MEASURES</span></div>
  <div class="block navy vertical" style="left:57px;top:721px;width:55px;height:68px"><span>ARTEFACTS</span></div>

  <div class="block cream measure" style="left:115px;top:455px;width:233px;height:128px">
    <h4><span class="hl">PERFORMANCE:</span><br>AIP MEASURABLE/DESIRED OUTCOMES ENGAGEMENT:</h4>
    <ul class="ticks">
      <li>10% Reduction in behaviour incidents</li><li>8% SDA rate- whole school</li><li>90% Attendance</li>
      <li>Improved student retention</li><li>VET- 100% CERT II</li><li>Out of Catchment enrolments &lt;20% (24% in 2025)</li>
    </ul>
  </div>
  <div class="block yellow measure" style="left:350px;top:455px;width:259px;height:128px">
    <h4 style="margin-top:9px">AIP MEASURABLE/DESIRED OUTCOMES ENGAGEMENT:</h4>
    <ul class="ticks">
      <li>10% Reduction in behaviour incidents</li><li>8% SDA rate- whole school</li><li>90% Attendance</li>
      <li>Improved student retention</li><li>VET- 100% CERT II</li><li>Out of Catchment enrolments &lt;20% (24% in 2025)</li>
    </ul>
  </div>
  <div class="block cream measure" style="left:612px;top:455px;width:373px;height:128px">
    <h4 style="margin-top:9px">LONG TERM MEASURABLE/DESIRED OUTCOMES:</h4>
    <ul class="ticks">
      <li>Increase in proportion of students achieving a C and above in all subjects with a focus on English and Maths</li>
      <li>Increase in proportion of students achieving an A or B in all subjects with a focus on English and Maths</li>
      <li>Maintain 100% of students achieving a SCE/ SCIA</li>
      <li>Improved rates of student attendance- days of learning</li>
      <li>Reduction in school disciplinary absence rates</li>
      <li>Improved Year 13 Next Steps Results</li>
      <li>Improved First Nations Outcomes- Closing the Gap- attendance and academic outcomes</li>
      <li>Improved participation and performance in NATEST</li>
    </ul>
  </div>
  <div class="block yellow measure" style="left:988px;top:455px;width:179px;height:128px">
    <h4 style="margin-top:9px">AIP MEASURABLE/DESIRED OUTCOMES PERFORMANCE (WHOLE SCHOOL):</h4>
    <ul class="ticks">
      <li>45% A-B</li><li>90% A-C</li><li>100% A-D</li><li>100% SCE/SCIA (Year 12 2026)</li>
    </ul>
  </div>

  <div class="block ice measure" style="left:115px;top:586px;width:233px;height:131px">
    <h4><span class="hl">BEHAVIOUR :</span><br>STAFF WILL</h4>
    <ul class="ticks">
      <li>Apply the Critical Routines, Essential Skills for Classroom Management and How Tallow Students Learn</li>
      <li>Access agreed data sets to know their learners, plan and differentiate to ensure accessibility for all students</li>
      <li>Use Multi Tiered Systems of Support and the Student Referral Team to support behaviour, academics, and wellbeing to improve outcomes for students</li>
      <li>Utilise SkyLearn for all 7, 8, Senior School Submissions and VET classes from 2026</li>
    </ul>
  </div>
  <div class="block sky measure" style="left:350px;top:586px;width:259px;height:131px">
    <h4 style="margin-top:9px">STUDENTS WILL</h4>
    <ul class="ticks">
      <li>Be prepared and ready for learning and follow Critical Routines</li>
      <li>Know, <b>what</b>, <b>how</b> and <b>why</b> they are learning</li>
    </ul>
  </div>
  <div class="block ice measure" style="left:612px;top:586px;width:373px;height:131px">
    <h4 style="margin-top:9px">EDUCATION SUPPORT OFFICERS WILL</h4>
    <ul class="ticks">
      <li>Maximise their time in classrooms with students- face to face</li>
      <li>Support the students in classrooms, in year level hubs, in the reset room and in alternative learning environments.</li>
    </ul>
  </div>
  <div class="block sky measure" style="left:988px;top:586px;width:179px;height:131px">
    <h4 style="margin-top:9px">LEADERSHIP TEAM WILL</h4>
    <ul class="ticks">
      <li>Support all teaching and non- teaching staff</li><li>Demonstrate Instructional Leadership</li>
      <li>Display visible leadership in the classroom/s.</li>
    </ul>
  </div>

  <div class="block cream panel" style="left:115px;top:721px;width:485px;height:58px;border-radius:0 0 8px 0">
    <ul class="ticks">
      <li>Moderation Plan- Before, After, End, including a HOD planned collaboration cycle</li>
      <li>Staff Collaborative Planning Outcomes</li><li>Three Levels of Planning</li><li>Curriculum Aligned Marking Guides</li>
    </ul>
  </div>
  <div class="block ice panel" style="left:622px;top:721px;width:545px;height:58px;border-radius:0 0 8px 0">
    <ul class="ticks">
      <li>SkyLearn - Resourcing and Unit Plans</li><li>AARAs</li><li>Assessment Calendar</li><li>Maximising Learning Team Outcomes</li>
    </ul>
  </div>
</section>

<!-- Red tape -->
<section>
  <div class="block navy redtape-label" style="left:34px;top:799px;width:152px;height:50px">REDUCTION OF RED TAPE IN<br>DAY-TO-DAY WORK, PLANNING<br>AND PROCESSES INCLUDE</div>
  <div class="block cream redtape" style="left:186px;top:799px;width:981px;height:50px">
    <ul class="ticks">
      <li>Tallow Strategy – Ask: Is this the best way to do it? How do we keep it simple?</li>
      <li>Strategic Meeting Scheduling</li><li>Investigate assessment submission</li>
    </ul>
    <ul class="ticks">
      <li>NCCD data collection to be reviewed</li>
      <li>Increase use of StudyPath- for student work at home requirements</li>
    </ul>
  </div>
</section>

</body>
</html>
```